Letterhead and compliment slip

We are a UK-based market research agency. We are looking for a new letterhead design to incorporate our logo, address details and company information. We are looking for a simple design. It should be modern. It needs to have a qualify feel. As we are UK based it needs to be designed for A4 paper size (letterhead).
I'm really looking for something simple in design terms!
Both letterhead and compliment slip need to include:
Our logo
Company address
Telephone number
Email address
Website address
Company registration number
VAT registration number
Grey and green would be a good colour scheme to fit with our logo

```html
<!DOCTYPE html>
<html lang="en">
<head>
<meta charset="utf-8">
<title>Northvale Insight – Letterhead and Compliment Slip</title>
<link rel="stylesheet" href="https://fonts.googleapis.com/css2?family=Open+Sans:wght@400;600;700&family=Lato:ital,wght@0,400;1,400&display=swap">
<style>
  :root {
    --green: #9dc43a;
    --green-dark: #8ab42c;
    --grey: #a7a8ab;
    --grey-dark: #7d7e82;
    --ink: #3b3b3d;
    --paper: #ffffff;
    --backdrop: #e4e5e7;
  }
  * { margin: 0; padding: 0; box-sizing: border-box; }
  html, body { width: 1200px; height: 917px; overflow: hidden; background: var(--backdrop); }
  body { position: relative; font-family: "Open Sans", Arial, sans-serif; color: var(--ink); }

  .sheet { position: absolute; background: var(--paper); overflow: hidden; }

  /* Letterhead */
  .letterhead { left: 104px; top: 142px; width: 486px; height: 627px; }
  .brand { position: absolute; display: flex; align-items: center; gap: 7px; }
  .brand-dot { width: 20px; height: 20px; border-radius: 50%; background: var(--green); }
  .brand-name { font-family: "Open Sans", Arial, sans-serif; font-weight: 700; font-size: 22px; color: var(--green); letter-spacing: -0.3px; }
  .letterhead .brand { left: 45px; top: 26px; }

  .contact-block { position: absolute; left: 316px; top: 26px; height: 32px; border-left: 1px solid #c9c9cb; padding-left: 10px; font-size: 8.6px; line-height: 10.6px; color: var(--ink); }
  .contact-block li { list-style: none; display: flex; align-items: center; gap: 4px; }
  .contact-block svg { width: 7px; height: 7px; fill: var(--green); flex: none; }

  .letter { position: absolute; left: 45px; top: 118px; width: 396px; font-size: 7.6px; line-height: 9.4px; color: #4a4a4c; }
  .letter .date { margin-bottom: 9px; }
  .letter .recipient { margin-bottom: 26px; }
  .letter .greeting { margin-bottom: 18px; }
  .letter .body p { line-height: 14px; margin-bottom: 14px; }
  .letter .closing { margin-top: 26px; }
  .signature-mark { width: 112px; height: 14px; margin: 6px 0 6px; background: linear-gradient(90deg, #f1f1f2, #e2e2e4); border-radius: 2px; }
  .signer-name { font-size: 10px; font-weight: 400; color: var(--ink); line-height: 12px; }
  .signer-role { margin-top: 4px; }

  .letter-footer { position: absolute; left: 0; bottom: 0; width: 486px; height: 100px; }
  .footer-reg { position: absolute; left: 45px; top: 598px; font-size: 9.6px; line-height: 11.6px; color: #fff; }
  .footer-address { position: absolute; right: 28px; top: 581px; text-align: right; font-size: 9.6px; line-height: 11.4px; color: #fff; }
  .footer-address strong { font-weight: 600; }

  /* Compliment slip */
  .slip { left: 610px; top: 524px; width: 488px; height: 244px; font-family: "Lato", "Open Sans", sans-serif; }
  .slip .brand { left: 30px; top: 30px; }
  .slip-reg { position: absolute; left: 311px; top: 36px; font-size: 9.6px; line-height: 11.6px; color: #222; }
  .slip-contact { position: absolute; left: 29px; top: 158px; font-size: 9.4px; line-height: 11.4px; color: #222; }
  .slip-rule { position: absolute; left: 29px; top: 196px; width: 318px; height: 1px; background: var(--green); }
  .slip-tagline { position: absolute; left: 354px; top: 186px; font-style: italic; font-size: 13.5px; color: var(--green); }
  .slip-address { position: absolute; left: 29px; top: 202px; font-size: 9.2px; line-height: 11.6px; color: #222; }
  .slip-address .company { color: var(--green-dark); }
</style>
</head>
<body>

<section class="sheet letterhead" aria-label="A4 letterhead">
  <div class="brand">
    <span class="brand-dot"></span>
    <span class="brand-name">Northvale Insight</span>
  </div>

  <ul class="contact-block">
    <li><svg viewBox="0 0 10 10"><path d="M2 1l2 2-1 1.5c.7 1.3 1.5 2.1 2.5 2.5L7 6l2 2-1.5 1.5C4 9 1 6 .5 2.5z"/></svg>+44 (0)1632 960418</li>
    <li><svg viewBox="0 0 10 10"><rect x="0" y="2" width="10" height="6.5"/><path d="M0 2l5 3.5L10 2" fill="none" stroke="#fff" stroke-width="1"/></svg>hello@northvaleinsight.co.uk</li>
    <li><svg viewBox="0 0 10 10"><circle cx="5" cy="5" r="4.6"/></svg>www.northvaleinsight.co.uk</li>
  </ul>

  <div class="letter">
    <p class="date">Issuing Date: May 5, 2018</p>
    <p class="recipient">Name Of Employee Mr. XYZABC<br>Address of Employee<br>Address Line 2 etc..</p>
    <p class="greeting">Dear Mr.XYZABC</p>
    <div class="body">
      <p>Lorem Ipsum has been the industry's standard dummy text ever since the 1500s, when an unknown printer took a galley of type and scrambled it to make a type specimen book. It has survived not only five centuries, but also the leap into electronic typesetting, remaining essentially unchanged. It was popularised in the 1960s with the release of Dryset sheets containing Lorem Ipsum passages, and more recently with desktop publishing software like Pagecraft including versions of Lorem Ipsum.</p>
      <p>Lorem Ipsum is simply dummy text of the printing and typesetting industry. Lorem Ipsum has been the industry's standard dummy text ever since the 1500s, when an unknown printer took a galley of type and scrambled it to make a type specimen book.</p>
      <p>It has survived not only five centuries, but also the leap into electronic typesetting, remaining essentially unchanged. It was popularised in the 1960s with the release of Dryset sheets containing Lorem Ipsum passages.</p>
    </div>
    <p class="closing">Yours Sincerely</p>
    <div class="signature-mark" role="img" aria-label="Handwritten signature of the managing director"></div>
    <p class="signer-name">Daniel Hartley</p>
    <p class="signer-role">Managing Director</p>
  </div>

  <svg class="letter-footer" viewBox="0 0 486 100" preserveAspectRatio="none" aria-hidden="true">
    <path d="M0 0 C40 25 120 45 220 40 C270 37 300 34 330 25 C240 40 160 50 100 44 C50 38 20 30 0 22 Z" fill="var(--grey)"/>
    <path d="M0 22 C60 42 150 52 240 44 C330 36 420 12 486 10 L486 100 L0 100 Z" fill="var(--green)"/>
  </svg>
  <p class="footer-reg">Registration number: 4817206<br>VAT registration number: 713562084</p>
  <p class="footer-address"><strong>Northvale Insight Ltd</strong><br>12 Willow Court, Station Road, Elmbridge<br>Elmbridge, Hertfordshire, HX4 2QL</p>
</section>

<section class="sheet slip" aria-label="Compliment slip">
  <div class="brand">
    <span class="brand-dot"></span>
    <span class="brand-name">Northvale Insight</span>
  </div>
  <p class="slip-reg">Registration number: 4817206<br>VAT registration number: 713562084</p>
  <p class="slip-contact">+44 (0)1632 960418<br>hello@northvaleinsight.co.uk<br>www.northvaleinsight.co.uk</p>
  <div class="slip-rule"></div>
  <p class="slip-tagline">With Compliments</p>
  <p class="slip-address"><span class="company">Northvale Insight Ltd.</span><br>12 Willow Court, Station Road, Elmbridge<br>Elmbridge, Hertfordshire, HX4 2QL</p>
</section>

</body>
</html>
```